Real Estate Marketing Postcards need a fresh look, Front & Back

I have a current postcard design (attached) that lacks design quality and too much use of color. I do like the basic color scheme, but I'm open to anything that cleans up the look and incorporates space for the existing text. I'm not opposed to a design with a white background, more white space. The design should be full bleed according to the attached specs. I would like this to be sent over in an Adobe format, something like InDesign.

The company logo will remain the same colors and appearance. The headshot will likely be updated in the coming weeks.

I am attaching a sample of a recent card plus a template from the printer showing the back of the card and location of the address and postage section that must remain blank. I am also including the logo and another logo designed for use with a white (or non blue) background.

(feel free to swap in stock photos of whatever house you want, but the front of the card should incorporate at least one photo of a house.)

Target Market(s)

Home owners.

Industry/Entity Type

Real Estate

Font styles to use
Sans Serif

Colors

Designer to choose colors to be used in the design.

Requirements
Must have
• Company logo, the headshot, the contact info on the back, a photo or photos of a house along with the text "Just Sold" or "Sold" featured on the front of the card.

```html
<!DOCTYPE html>
<html lang="en">
<head>
<meta charset="utf-8">
<title>Just Sold Postcard – Front &amp; Back</title>
<link href="https://fonts.googleapis.com/css2?family=Nunito:wght@700;800;900&family=Raleway:wght@400;500;600&family=Yellowtail&display=swap" rel="stylesheet">
<style>
  :root{
    --blue:#1f5d9c;
    --blue-deep:#0f4f8f;
    --lime:#c5dc2a;
    --red:#e3151b;
    --charcoal:#4a4a4d;
    --band:rgba(78,78,80,.92);
    --white:#ffffff;
    --rule:#9a9a9a;
    --page:#e6e6e6;
  }
  *{box-sizing:border-box;margin:0;padding:0}
  html,body{width:1200px;height:1200px;overflow:hidden}
  body{background:var(--page);font-family:'Raleway',sans-serif;position:relative}
  .card{position:absolute;left:200px;width:800px;height:565px;overflow:hidden;background:var(--white);box-shadow:0 3px 10px rgba(0,0,0,.18)}
  .card--front{top:10px}
  .card--back{top:605px}
  .abs{position:absolute}

  /* FRONT */
  .house-photo{left:0;top:0;width:800px;height:565px;
    background:linear-gradient(180deg,#f4f6f8 0%,#e4e9ee 30%,#c98f6a 42%,#e9d3b6 55%,#d8c2a4 68%,#4f7a34 80%,#6c9a3c 90%,#caa08c 100%)}
  .hero-tag{left:37px;top:0;width:227px;height:262px;background:var(--blue);text-align:center;color:var(--white);font-family:'Nunito',sans-serif;font-weight:900}
  .script{font-family:'Yellowtail',cursive;color:var(--lime);font-weight:400}
  .hero-tag .script{font-size:44px;display:block;margin-top:22px;line-height:1}
  .hero-tag .big{font-size:38px;line-height:44px;display:block;margin-top:14px}
  .hero-tag .small{font-size:24px;display:block;line-height:28px}
  .brand{right:75px;top:92px;color:var(--blue);font-family:'Nunito',sans-serif;font-weight:800;font-size:30px;line-height:1}
  .brand-sub{display:block;font-size:30px}
  .realtor-band{left:0;top:433px;width:585px;height:88px;background:var(--band)}
  .realtor-band h1{position:absolute;right:36px;top:8px;font-family:'Nunito',sans-serif;font-weight:900;font-size:44px;color:var(--lime);white-space:nowrap}
  .realtor-band p{position:absolute;right:36px;top:60px;font-family:'Nunito',sans-serif;font-weight:800;font-size:13px;color:var(--white)}
  .headshot-frame{background:var(--blue);padding:9px}
  .headshot-frame .photo{width:100%;height:100%;border:4px solid var(--white);background:linear-gradient(180deg,#b8b8c2 0%,#c9b7a8 55%,#e8e8ee 100%)}
  .front-headshot{left:585px;top:369px;width:166px;height:181px}

  /* BACK */
  .back-top{left:0;top:0;width:800px;height:372px;background:var(--charcoal)}
  .selling-band{left:0;top:23px;width:800px;height:70px;background:var(--blue-deep);display:flex;align-items:center;padding-left:40px;gap:16px}
  .selling-band .script{font-size:40px}
  .selling-band h2{font-family:'Nunito',sans-serif;font-weight:800;font-size:24px;color:var(--white)}
  .reasons{left:36px;top:114px;width:385px}
  .reasons h3,.contact h3{font-family:'Nunito',sans-serif;font-weight:900;color:var(--lime);line-height:1;white-space:nowrap}
  .reasons h3{font-size:24px}
  .reasons h3 .key{color:var(--red)}
  .reasons p.lead{font-family:'Nunito',sans-serif;font-weight:800;color:var(--white);font-size:16px;line-height:21px;margin-top:5px}
  .reason-box{left:45px;top:213px;width:356px;height:128px;border:1px solid #8a9a3a;border-radius:8px}
  .reason{position:absolute;left:-10px;display:flex;gap:9px;font-size:11px;line-height:14px;color:var(--white);width:350px}
  .reason .num{flex:0 0 19px;height:19px;border-radius:50%;background:var(--lime);color:var(--charcoal);font-weight:800;font-size:12px;display:flex;align-items:center;justify-content:center;font-family:'Nunito',sans-serif}
  .reason span.t{padding-top:2px;text-align:justify}
  .divider{left:425px;top:118px;width:1px;height:222px;background:#6b6b6e}
  .contact{left:445px;top:115px;width:340px}
  .contact h3{font-size:22px}
  .contact p{font-family:'Nunito',sans-serif;font-weight:800;color:var(--white);font-size:15px;line-height:19px;margin-top:3px}
  .contact-strip{left:425px;top:254px;width:375px;height:86px;background:var(--blue-deep)}
  .back-headshot{left:445px;top:203px;width:103px;height:127px;padding:6px;border:1px solid #aac}
  .agent{left:562px;top:203px;color:var(--white);font-size:12.5px;line-height:17px}
  .agent .name{color:var(--lime);font-family:'Nunito',sans-serif;font-weight:800}
  .details{left:562px;top:266px;color:var(--white);font-size:12px;line-height:18.5px;list-style:none}
  .details li{display:flex;align-items:center;gap:6px}
  .details svg{width:10px;height:10px;fill:var(--lime)}
  .accent-line{left:60px;top:372px;width:680px;height:6px;background:var(--lime);border-radius:0 0 3px 3px}
  .back-brand{left:40px;top:470px;color:var(--blue);font-family:'Nunito',sans-serif;font-weight:800;font-size:22px;line-height:1}
  .address-line{left:237px;width:383px;height:1px;background:var(--rule)}
  .stamp{left:666px;top:428px;width:95px;height:95px;border:1px solid #b5b5b5}
</style>
</head>
<body>

<section class="card card--front" aria-label="Postcard front">
  <div class="abs house-photo" role="img" aria-label="Photo of a sold Mediterranean-style house with tiled roof, front lawn and paver driveway"></div>
  <div class="abs hero-tag">
    <span class="script">Just Sold</span>
    <span class="big">Another<br>HOME</span>
    <span class="small">JUST LISTED by</span>
  </div>
  <div class="abs brand">Alderbrook<span class="brand-sub">Real Estate</span></div>
  <div class="abs realtor-band">
    <h1>The Ashgrove Realtor</h1>
    <p>YOU KNOW IT WON'T LAST LONG!</p>
  </div>
  <div class="abs headshot-frame front-headshot">
    <div class="photo" role="img" aria-label="Agent headshot"></div>
  </div>
</section>

<section class="card card--back" aria-label="Postcard back">
  <div class="abs back-top"></div>
  <div class="abs selling-band">
    <span class="script">Selling?</span>
    <h2>Choosing the right agent is critical to your success.</h2>
  </div>

  <div class="abs reasons">
    <h3>THERE ARE <span class="key">3 KEY</span> REASONS</h3>
    <p class="lead">a home doesn't sell, and #1 is Choosing the<br>wrong agent to market your property.</p>
  </div>
  <div class="abs reason-box">
    <div class="reason" style="top:6px"><span class="num">1</span><span class="t">Your home is your biggest asset.</span></div>
    <div class="reason" style="top:35px"><span class="num">2</span><span class="t">You owe it to yourself to have every advantage by choosing the local agent with the expertise to position your Ashgrove home and get it sold fast and for top dollar.</span></div>
    <div class="reason" style="top:94px"><span class="num">3</span><span class="t">There is no other agent who knows the Ashgrove market better. Contact me today to get your home SOLD.</span></div>
  </div>

  <div class="abs divider"></div>
  <div class="abs contact">
    <h3>CONTACT ME TODAY</h3>
    <p>to discuss your home's value and what steps<br>I will take to assure your success.</p>
  </div>
  <div class="abs contact-strip"></div>
  <div class="abs headshot-frame back-headshot">
    <div class="photo" role="img" aria-label="Agent headshot"></div>
  </div>
  <div class="abs agent">
    <div class="name">DARIO VENTURELLI</div>
    <div>The Ashgrove Realtor</div>
    <div>Principal Broker</div>
  </div>
  <ul class="abs details">
    <li><svg viewBox="0 0 10 10"><path d="M5 0 10 5H8.5V10H6V7H4V10H1.5V5H0Z"/></svg>REALTOR Alderbrook Real Estate</li>
    <li><svg viewBox="0 0 10 10"><path d="M2 0 4 2.5 3 4Q4.5 6.5 6 7L7.5 6 10 8 8.5 10Q3 9.5 0 1.5Z"/></svg>(555) 310-4400 (Office)</li>
    <li><svg viewBox="0 0 10 10"><path d="M2 0 4 2.5 3 4Q4.5 6.5 6 7L7.5 6 10 8 8.5 10Q3 9.5 0 1.5Z"/></svg>(555) 862-1907</li>
    <li><svg viewBox="0 0 10 10"><circle cx="5" cy="5" r="4.3" fill="none" stroke="#c5dc2a" stroke-width="1.2"/><path d="M.7 5H9.3M5 .7V9.3" stroke="#c5dc2a" stroke-width="1"/></svg>www.AshgroveHomes.com</li>
  </ul>

  <div class="abs accent-line"></div>
  <div class="abs back-brand">Alderbrook<br>Real Estate</div>
  <div class="abs address-line" style="top:440px"></div>
  <div class="abs address-line" style="top:480px"></div>
  <div class="abs address-line" style="top:523px"></div>
  <div class="abs stamp"></div>
</section>

</body>
</html>
```